Wordpress Template Design using existing Logo and Colors

We are wanting a wordpress theme designing for our b2b marketing consultancy business. A comprehesive and elagant design to our current site www.pelvarogroup.com would be good.

Industry/Entity Type

Marketing

Font styles to use
Sans Serif

```html
<!DOCTYPE html>
<html lang="en">
<head>
<meta charset="utf-8">
<title>Pelvaro – B2B Data &amp; Marketing</title>
<link href="https://fonts.googleapis.com/css2?family=Montserrat:wght@600;700&family=Roboto:wght@400;500;700&display=swap" rel="stylesheet">
<style>
:root{
  --red:#ec1c24;
  --red-soft:#f03a40;
  --ink:#2b2f36;
  --slate:#4a5058;
  --text:#555b63;
  --dark:#15191f;
  --footer:#1b2129;
  --footer-bar:#12161c;
  --light:#f2f3f5;
  --grey-btn:#5a6069;
  --white:#ffffff;
}
*{box-sizing:border-box;margin:0;padding:0}
html,body{width:1200px;height:2350px;overflow:hidden;background:var(--white)}
body{font-family:"Roboto",Arial,sans-serif;color:var(--text);position:relative}
.abs{position:absolute}

/* header */
.brand{left:140px;top:44px;display:flex;align-items:center;gap:10px}
.brand-mark{width:14px;height:14px;background:var(--red)}
.brand-name{font:700 34px/1 "Roboto",sans-serif;color:var(--red);letter-spacing:1px}
.top-phones{top:19px;right:132px;display:flex;gap:11px}
.top-phone{height:27px;padding:0 13px;font:500 13px/27px "Roboto",sans-serif;color:var(--white);border-radius:2px;white-space:nowrap}
.top-phone.us{background:var(--red)}
.top-phone.sg{background:var(--grey-btn)}
.main-nav{top:66px;left:540px;display:flex;gap:30px;font:500 11.5px/1 "Roboto",sans-serif;color:var(--ink);text-transform:uppercase;white-space:nowrap}
.search-icon{left:1052px;top:64px}

/* hero */
.hero-bg{left:0;top:100px;width:1200px;height:470px;background:linear-gradient(180deg,#fff 0%,#f4f5f7 100%)}
.hero-photo{left:630px;top:100px;width:570px;height:463px;background:linear-gradient(180deg,#e8ecef 0%,#c9d1d8 45%,#eef0f2 100%)}
.hero-title{left:145px;top:222px;font:700 34px/50px "Montserrat",sans-serif;color:var(--red);white-space:nowrap}
.hero-title .dark{color:var(--slate)}
.hero-lead{left:145px;top:390px;width:460px;font:400 12.5px/20px "Roboto",sans-serif;color:var(--ink)}
.btn{display:block;text-align:center;text-transform:uppercase;color:var(--white);font:500 11px "Roboto",sans-serif;letter-spacing:.3px;white-space:nowrap}
.hero-btn{left:146px;top:444px;width:120px;height:36px;line-height:36px;background:var(--red)}
.slider-dots{left:146px;top:503px;display:flex;gap:14px;align-items:center}
.slider-dots span{width:8px;height:8px;border-radius:50%;background:#8b9097}
.slider-dots .on{width:14px;height:14px;border:3px solid #c8ccd1;background:#8b9097}

/* about */
.about{left:0;top:560px;width:1200px;height:445px}
.about-title{left:155px;top:644px;font:700 15px/1 "Roboto",sans-serif;color:var(--white);text-transform:uppercase}
.about-text{left:155px;top:672px;width:520px;font:400 11px/20.5px "Roboto",sans-serif;color:var(--white)}
.about-text p+p{margin-top:4px}
.about-btn{left:155px;top:905px;width:97px;height:33px;line-height:33px;background:var(--dark)}
.about-photo{left:712px;top:588px;width:335px;height:413px;background:linear-gradient(180deg,#d9c4b4 0%,#3f6f76 45%,#5a5e66 100%);border-radius:140px 140px 0 0}

/* why */
.why{left:0;top:1001px;width:1200px;height:258px;background:linear-gradient(180deg,#1a1d22 0%,#0b0c0e 100%)}
.why-title{left:0;top:1037px;width:1200px;text-align:center;font:700 15px/1 "Roboto",sans-serif;color:var(--white);text-transform:uppercase}
.why-text{left:245px;top:1067px;width:710px;text-align:center;font:400 11px/19px "Roboto",sans-serif;color:#e4e6e9}
.lower-bg{left:0;top:1259px;width:1200px;height:650px;background:linear-gradient(160deg,#f7f8f9 0%,#eceef1 100%)}
.lower-shape{left:0;top:1560px;width:360px;height:350px;background:#e3e6ea;clip-path:polygon(0 40%,100% 0,100% 100%,0 100%)}

.service-card{width:207px;background:var(--white);border-top:3px solid var(--red);box-shadow:0 4px 14px rgba(0,0,0,.1);text-align:center;padding:22px 14px 0}
.service-card h3{font:700 11px/1 "Roboto",sans-serif;color:var(--ink);text-transform:uppercase;margin:14px 0 10px}
.service-card p{font:400 10.5px/17px "Roboto",sans-serif;color:var(--text)}
.service-card .card-btn{margin:14px auto 0;width:74px;height:24px;line-height:24px;font-size:9px;background:var(--red)}
.card-1{left:134px;top:1172px;height:202px}
.card-2{left:374px;top:1172px;height:202px}
.card-3{left:614px;top:1163px;height:221px;padding-top:18px}
.card-4{left:861px;top:1172px;height:202px}

/* team */
.team-title{left:0;top:1428px;width:1200px;text-align:center;font:700 15px/1 "Roboto",sans-serif;color:var(--ink);text-transform:uppercase}
.team-text{left:190px;top:1458px;width:820px;text-align:center;font:400 11px/19px "Roboto",sans-serif;color:var(--text)}
.member-photo{width:210px;height:210px;border:4px solid var(--white);box-shadow:0 2px 10px rgba(0,0,0,.12)}
.member-name{width:210px;text-align:center;font:500 13px/1 "Roboto",sans-serif;color:var(--ink)}

/* brochure */
.brochure{left:0;top:1908px;width:1200px;height:141px;background:linear-gradient(90deg,#e8232b 0%,#f0383f 100%)}
.brochure-art{left:182px;top:1940px;width:116px;height:84px;background:linear-gradient(180deg,#f7c9cb 0%,#fbe6e7 100%)}
.brochure-title{left:329px;top:1953px;font:700 15px/1 "Roboto",sans-serif;color:var(--white);text-transform:uppercase}
.brochure-text{left:329px;top:1979px;width:460px;font:400 11px/18px "Roboto",sans-serif;color:#fde3e4}
.brochure-btn{left:819px;top:1961px;width:194px;height:43px;line-height:43px;background:var(--footer);font-weight:700;font-size:11.5px}

/* footer */
.footer{left:0;top:2049px;width:1200px;height:268px;background:var(--footer)}
.footer-col{top:2100px;width:215px}
.footer-col h4{font:700 11px/1 "Roboto",sans-serif;color:var(--white);text-transform:uppercase;margin-bottom:22px}
.footer-col ul{list-style:none}
.footer-col li{display:flex;gap:12px;font:400 10.5px/16px "Roboto",sans-serif;color:#d7dade;margin-bottom:9px}
.footer-col li svg{flex:0 0 10px;margin-top:3px}
.footer-col p{font:400 10.5px/17px "Roboto",sans-serif;color:#d7dade}
.footer-col .holiday{color:var(--red);margin-left:22px;margin-top:6px}
.col-global{left:141px}.col-regional{left:376px}.col-hours{left:617px}.col-news{left:849px}
.news-input{margin-top:18px;width:198px;height:32px;border:1px solid #3a424d;padding:0 10px;font:400 9px/30px "Roboto",sans-serif;color:#7b838d}
.news-btn{margin-top:10px;width:78px;height:26px;line-height:26px;background:var(--red)}
.footer-bar{left:0;top:2317px;width:1200px;height:33px;background:var(--footer-bar)}
.copyright{left:147px;top:2328px;font:400 9px/1 "Roboto",sans-serif;color:#9aa1aa}
.social{left:930px;top:2324px;display:flex;gap:10px}
.social span{width:14px;height:14px;border-radius:2px}
</style>
</head>
<body>

<!-- header -->
<div class="abs brand"><span class="brand-mark"></span><span class="brand-name">PELVARO</span></div>
<div class="abs top-phones"><span class="top-phone us">+1 (555) 214-7730</span><span class="top-phone sg">+65 6100 4287</span></div>
<nav class="abs main-nav"><span>Home</span><span>About Us</span><span>Target Marketing</span><span>Data Management</span><span>Contact Us</span></nav>
<svg class="abs search-icon" width="13" height="13" viewBox="0 0 13 13"><circle cx="5.5" cy="5.5" r="4" fill="none" stroke="#2b2f36" stroke-width="1.6"/><line x1="8.5" y1="8.5" x2="12" y2="12" stroke="#2b2f36" stroke-width="1.6"/></svg>

<!-- hero -->
<div class="abs hero-bg"></div>
<div class="abs hero-photo" role="img" aria-label="Businessman standing at a glass balcony overlooking a city skyline"></div>
<h1 class="abs hero-title">Reach The Right People,<br>With The Right Message,<br><span class="dark">At The Right Time</span></h1>
<p class="abs hero-lead">Whether your aim is to acquire new customers, re-engage existing, or grow their value over time, Pelvaro offers tailored solutions</p>
<a class="abs btn hero-btn">Learn More</a>
<div class="abs slider-dots"><span class="on"></span><span></span><span></span><span></span></div>

<!-- about -->
<svg class="abs about" width="1200" height="445" viewBox="0 0 1200 445"><polygon points="0,3 1200,25 1200,445 0,445" fill="#ec1c24"/><polygon points="0,3 480,60 900,20 1200,25 1200,120 700,90 0,160" fill="#f0383f" opacity=".5"/></svg>
<h2 class="abs about-title">About Pelvaro</h2>
<div class="abs about-text">
<p>Pelvaro is the primary source of market intelligence focused on identifying business opportunities and key decision makers throughout Asia Pacific Region. We provide access to over 3.5 million decision makers across 1.5 million profiled organizations in 23 Asia Pacific countries. With our local presence in 8 countries, we provide tailored target marketing programs in Asia Pacific Region.</p>
<p>Lorem ipsum dolor sit amet, consectetuer adipiscing elit. Aenean commodo ligula eget dolor. Aenean massa. Cum sociis natoque penatibus et magnis dis parturient montes, nascetur ridiculus mus. Donec quam felis, ultricies nec, pellentesque eu, pretium quis, sem. Nulla consequat massa quis enim. Donec pede justo, fringilla vel, aliquet nec, vulputate eget, arcu</p>
</div>
<a class="abs btn about-btn">Read More</a>
<div class="abs about-photo" role="img" aria-label="Two smiling business colleagues looking at a tablet"></div>

<!-- why choose us -->
<div class="abs why" role="img" aria-label="Dark photo of a business meeting in silhouette"></div>
<h2 class="abs why-title">Why Choose Us...?</h2>
<p class="abs why-text">We are a B2B Data, Analytics and Marketing Consulting Company specialized in harnessing the power of potential data to strengthen connections between decisions makers, companies and products. We focus on solutions engineered to solve distinct challenges in the data, direct marketing, and analytics space.</p>
<div class="abs lower-bg"></div>
<div class="abs lower-shape"></div>

<div class="abs service-card card-1">
<svg width="44" height="44" viewBox="0 0 44 44" fill="none" stroke="#ec1c24" stroke-width="1.6"><path d="M11 20a9 9 0 0 1 17-5a7 7 0 0 1 5 13H11a5 5 0 0 1 0-8z"/><ellipse cx="22" cy="27" rx="8" ry="3"/><path d="M14 27v10c0 1.7 3.6 3 8 3s8-1.3 8-3V27M14 32c0 1.7 3.6 3 8 3s8-1.3 8-3"/></svg>
<h3>B2B Database</h3>
<p>Get access to Asia's leading market &amp; business intelligence database over 1,500,000 organizations and 3,500,000 decision makers.</p>
</div>
<div class="abs service-card card-2">
<svg width="44" height="44" viewBox="0 0 44 44" fill="none" stroke="#ec1c24" stroke-width="1.6"><circle cx="22" cy="22" r="15"/><circle cx="22" cy="22" r="9"/><path d="M22 2v8M22 34v8M2 22h8M34 22h8"/><circle cx="22" cy="20" r="2.5"/><path d="M18 27a4 4 0 0 1 8 0"/></svg>
<h3>Target Marketing</h3>
<p>We develop tailored marketing solutions based on your specific objectives, audience and budget to fetch high returns on investment.</p>
</div>
<div class="abs service-card card-3">
<svg width="44" height="44" viewBox="0 0 44 44" fill="none" stroke="#ec1c24" stroke-width="1.6"><path d="M8 24v-4a14 14 0 0 1 28 0v4"/><rect x="5" y="22" width="7" height="11" rx="2"/><rect x="32" y="22" width="7" height="11" rx="2"/><path d="M36 33v3a4 4 0 0 1-4 4h-7"/><rect x="19" y="38" width="6" height="4" rx="1"/></svg>
<h3>Call Centre</h3>
<p>When your business requires instantaneous and cost effective contact center, we are here to provide the necessary expertise.</p>
<a class="btn card-btn">Read More</a>
</div>
<div class="abs service-card card-4">
<svg width="44" height="44" viewBox="0 0 44 44" fill="none" stroke="#ec1c24" stroke-width="1.6"><path d="M16 5l8 4v8l-8 4-8-4V9z"/><path d="M8 9l8 4 8-4M16 13v8"/><path d="M10 24l8 4v8l-8 4-8-4v-8z"/><path d="M2 28l8 4 8-4M10 32v8"/><path d="M32 22l8 4v8l-8 4-8-4v-8z"/><path d="M24 26l8 4 8-4M32 30v8"/></svg>
<h3>Data Management</h3>
<p>We analyze your data and report on effective strategies for turning the data into a profitable resource.</p>
</div>

<!-- team -->
<h2 class="abs team-title">Our Experienced Team of Experts</h2>
<p class="abs team-text">Our experienced team of data experts are passionate about turning the morass of unstructured data into actionable intelligence. The core team consists of regionally and globally experienced executives and technology specialists. Each team member possesses industry knowledge and builds creative marketing solutions for our client's specific needs. The unique combination of the Local, Regional and Global mix, adds value by introducing diverse approaches and numerous perspectives in order to make our innovative solutions work best for our customers.</p>

<div class="abs member-photo" style="left:131px;top:1577px;background:linear-gradient(180deg,#eceae8 0%,#d8d3ce 100%)" role="img" aria-label="Portrait of a team member in a white t-shirt"></div>
<div class="abs member-name" style="left:131px;top:1800px">Daniel Hartley</div>
<div class="abs member-photo" style="left:376px;top:1609px;background:linear-gradient(180deg,#6f6a64 0%,#b7ada2 100%)" role="img" aria-label="Portrait of a team member in a casual shirt"></div>
<div class="abs member-name" style="left:376px;top:1832px">Marco Velden</div>
<div class="abs member-photo" style="left:612px;top:1577px;background:linear-gradient(180deg,#e9ebee 0%,#c9b8a6 100%)" role="img" aria-label="Portrait of a smiling team member holding a book"></div>
<div class="abs member-name" style="left:612px;top:1800px">Claire Osborne</div>
<div class="abs member-photo" style="left:857px;top:1614px;background:linear-gradient(180deg,#f1f1f1 0%,#6e7ea8 100%)" role="img" aria-label="Portrait of a smiling team member in a striped top"></div>
<div class="abs member-name" style="left:857px;top:1836px">Priya Ramanath</div>

<!-- brochure -->
<div class="abs brochure"></div>
<div class="abs brochure-art" role="img" aria-label="Illustration of folded corporate brochures"></div>
<h2 class="abs brochure-title">Corporate Brochure</h2>
<p class="abs brochure-text">Learn our leading target marketing and intelligent data management solutions to attain new customers for your niche products and services.</p>
<a class="abs btn brochure-btn">Download the Brochure</a>

<!-- footer -->
<div class="abs footer"></div>
<div class="abs footer-col col-global">
<h4>Global HQ</h4>
<ul>
<li><svg width="10" height="10" viewBox="0 0 10 10"><path d="M2 0l2 2.5-1 1.5a6 6 0 0 0 3 3l1.5-1L10 8l-1.5 2C4 10 0 6 0 1.5z" fill="#ec1c24"/></svg>+1 (555) 214-7730</li>
<li><svg width="10" height="10" viewBox="0 0 10 10"><rect y="1.5" width="10" height="7" fill="#ec1c24"/><path d="M0 2l5 3.5L10 2" stroke="#1b2129" fill="none"/></svg>hello.us@pelvarogroup.com</li>
<li><svg width="10" height="10" viewBox="0 0 10 10"><circle cx="5" cy="5" r="4.3" fill="none" stroke="#ec1c24" stroke-width="1.2"/><path d="M.7 5h8.6M5 .7c-2.4 2.6-2.4 6 0 8.6M5 .7c2.4 2.6 2.4 6 0 8.6" stroke="#ec1c24" fill="none" stroke-width=".8"/></svg>www.pelvarogroup.com</li>
<li><svg width="10" height="10" viewBox="0 0 10 10"><path d="M5 10C2 6 1.5 5 1.5 3.5a3.5 3.5 0 0 1 7 0C8.5 5 8 6 5 10z" fill="#ec1c24"/><circle cx="5" cy="3.6" r="1.2" fill="#1b2129"/></svg>1840 Harbor Crest Lane, Suite 204,<br>Oakvale, CA 90412-3300, USA</li>
</ul>
</div>
<div class="abs footer-col col-regional">
<h4>Regional HQ</h4>
<ul>
<li><svg width="10" height="10" viewBox="0 0 10 10"><path d="M2 0l2 2.5-1 1.5a6 6 0 0 0 3 3l1.5-1L10 8l-1.5 2C4 10 0 6 0 1.5z" fill="#ec1c24"/></svg>+65 6100 4287</li>
<li><svg width="10" height="10" viewBox="0 0 10 10"><rect y="1.5" width="10" height="7" fill="#ec1c24"/><path d="M0 2l5 3.5L10 2" stroke="#1b2129" fill="none"/></svg>hello.sg@pelvarogroup.com</li>
<li><svg width="10" height="10" viewBox="0 0 10 10"><circle cx="5" cy="5" r="4.3" fill="none" stroke="#ec1c24" stroke-width="1.2"/><path d="M.7 5h8.6M5 .7c-2.4 2.6-2.4 6 0 8.6M5 .7c2.4 2.6 2.4 6 0 8.6" stroke="#ec1c24" fill="none" stroke-width=".8"/></svg>www.pelvarogroup.com</li>
<li><svg width="10" height="10" viewBox="0 0 10 10"><path d="M5 10C2 6 1.5 5 1.5 3.5a3.5 3.5 0 0 1 7 0C8.5 5 8 6 5 10z" fill="#ec1c24"/><circle cx="5" cy="3.6" r="1.2" fill="#1b2129"/></svg>22 Kemra Avenue 3, #08-14 Lumen<br>Park, Singapore 409921</li>
</ul>
</div>
<div class="abs footer-col col-hours">
<h4>Working Hours</h4>
<p>We work weekdays. Please contact us<br>for any enquiry</p>
<ul style="margin-top:12px">
<li><svg width="10" height="10" viewBox="0 0 10 10"><circle cx="5" cy="5" r="4.3" fill="none" stroke="#ec1c24" stroke-width="1.2"/><path d="M5 2.5V5l2 1.2" stroke="#ec1c24" fill="none" stroke-width="1.1"/></svg>Monday – Friday : 9AM – 6PM</li>
</ul>
<p class="holiday">Weekdends Holiday</p>
</div>
<div class="abs footer-col col-news">
<h4>Newsletter</h4>
<p>Subscribe to our newsletter for latest<br>updates about our company</p>
<div class="news-input">Your E-mail address</div>
<a class="btn news-btn">Subscribe</a>
</div>
<div class="abs footer-bar"></div>
<p class="abs copyright">Copyright © 2010 - 2018 Pelvaro. All Rights Reserved.</p>
<div class="abs social"><span style="background:#3b5b98"></span><span style="background:#2a9fd8"></span><span style="background:#2f6ea8"></span><span style="background:#e0282d"></span><span style="background:#f07a22"></span></div>

</body>
</html>
```